Business Card Design Project

I have established a company called "Tidewell" which is a business specialising in psychotherapy/counselling , predominantly for anxiety & depression.

My name is Mel....hence, the Tidewell link. However, Tidewell was also chosen for its reference to green shoots of growth/recovery.

Tidewell is to be "upmarket" and highly professional. I'm keen for the style and colours to reflect this.....taupe/grey with navy/black script, for example.....NO primary colours.

My name needs to be on the card and my mobile number. Not sure, but suspect it should also have my qualifications ( BA (Psych) & BSc (Hons) Psychology). Mobile number 0463 918 207.

```html
<!DOCTYPE html>
<html lang="en">
<head>
<meta charset="utf-8">
<title>Tidewell – Business Card</title>
<link href="https://fonts.googleapis.com/css2?family=Montserrat:wght@300;400;600&display=swap" rel="stylesheet">
<style>
  :root {
    --backdrop: #3c3c3c;
    --card-light: #fbfbfa;
    --card-dark: #1b1b1b;
    --ink: #4f4f4f;
    --ink-soft: #6a6a6a;
    --taupe-brown: #6b4a35;
    --wordmark: #6e5140;
    --bar-grey: #d6d5d2;
    --bar-olive: #3a3831;
    --tab-grey: #3d3c36;
  }
  * { margin: 0; padding: 0; box-sizing: border-box; }
  html, body {
    width: 1200px; height: 1000px; overflow: hidden;
    background: var(--backdrop);
    font-family: "Montserrat", sans-serif;
  }
  .stage { position: relative; width: 1200px; height: 1000px; }
  .card {
    position: absolute; width: 530px; height: 304px;
    border-radius: 14px; overflow: hidden;
  }
  .card--front { left: 206px; top: 164px; background: var(--card-light); color: var(--ink); }
  .card--back { left: 472px; top: 534px; background: var(--card-dark); }

  .accent { position: absolute; }
  .accent--top-grey { left: 28px; top: 0; width: 233px; height: 14px; background: var(--bar-grey); }
  .accent--corner-square { right: 0; top: 228px; width: 22px; height: 26px; background: var(--taupe-brown); }
  .accent--top-brown { right: 0; top: 0; width: 183px; height: 13px; background: var(--taupe-brown); }
  .accent--top-olive { right: 0; top: 13px; width: 108px; height: 25px; background: var(--bar-olive); }
  .accent--side-tab { left: 0; top: 186px; width: 12px; height: 55px; background: var(--tab-grey); }

  .holder-name {
    position: absolute; left: 37px; top: 151px;
    font-size: 19px; font-weight: 300; letter-spacing: 0.5px; text-transform: uppercase;
  }
  .holder-quals {
    position: absolute; left: 37px; top: 177px;
    font-size: 12px; font-weight: 300; color: var(--ink-soft);
  }
  .contact { position: absolute; left: 37px; top: 214px; list-style: none; font-size: 14px; font-weight: 300; line-height: 20px; }
  .contact__label { display: inline-block; width: 21px; font-weight: 600; }
  .website {
    position: absolute; right: 43px; top: 232px;
    font-size: 13px; font-weight: 300; color: var(--taupe-brown);
  }
  .website strong { font-weight: 600; }

  .wordmark {
    position: absolute; left: 34px; top: 186px;
    font-size: 42px; font-weight: 400; letter-spacing: 2px;
    color: var(--wordmark); line-height: 1.2;
  }
</style>
</head>
<body>
<main class="stage">
  <section class="card card--front" aria-label="Business card front">
    <span class="accent accent--top-grey"></span>
    <h1 class="holder-name">Mel Harrow</h1>
    <p class="holder-quals">BA (Psych) &amp; BSc (Hons) Psychology</p>
    <ul class="contact">
      <li><span class="contact__label">M</span>0463 918 207</li>
      <li><span class="contact__label">E</span>m.harrow@tidewell.com</li>
    </ul>
    <p class="website">www.<strong>tidewell</strong>.com</p>
    <span class="accent accent--corner-square"></span>
  </section>

  <section class="card card--back" aria-label="Business card back">
    <span class="accent accent--top-brown"></span>
    <span class="accent accent--top-olive"></span>
    <span class="accent accent--side-tab"></span>
    <p class="wordmark">Tidewell</p>
  </section>
</main>
</body>
</html>
```